Corvell Tiling Solutions, QBCC 8471302, ABN 48290517736, Email corvelltiling@brindlemail.com,Mobile 04958142

Corvell Tiling Solutions, is the name of my wall and floor tiling company and the details above are needed on the business card. Im open to see what people come up with i really have no colour requirements or other design specs as long as its not too plain.

```html
<!DOCTYPE html>
<html lang="en">
<head>
<meta charset="utf-8">
<title>Corvell Tiling Solutions – Business Card</title>
<link href="https://fonts.googleapis.com/css2?family=Montserrat:wght@400;500;600;700&display=swap" rel="stylesheet">
<style>
  :root {
    --backdrop: #e4e4e4;
    --tile-blue: #3f4aa8;
    --tile-blue-deep: #3540a0;
    --tile-blue-light: #4a56b4;
    --card-white: #ffffff;
    --brand-red: #d6334c;
    --text-light: #ffffff;
  }
  * { box-sizing: border-box; margin: 0; padding: 0; }
  html, body {
    width: 1200px; height: 1000px; overflow: hidden;
    background: var(--backdrop);
    font-family: "Montserrat", Arial, sans-serif;
  }
  .canvas { position: relative; width: 1200px; height: 1000px; }

  .card {
    position: absolute;
    width: 490px; height: 280px;
    overflow: hidden;
    box-shadow: 3px 5px 8px rgba(0,0,0,0.35);
  }
  .card--front { left: 265px; top: 130px; background: var(--card-white); }
  .card--back  { left: 490px; top: 545px; }

  .tile-field {
    position: absolute; inset: 0;
    background: radial-gradient(circle at 60% 40%, var(--tile-blue-light), var(--tile-blue) 55%, var(--tile-blue-deep));
  }
  .card--front .tile-field { bottom: auto; height: 158px; }

  .holder { position: absolute; left: 238px; top: 20px; color: var(--text-light); }
  .holder__name { font-size: 15px; font-weight: 500; letter-spacing: 0.5px; }
  .holder__role { font-size: 8px; margin-top: 3px; opacity: 0.9; }

  .contact { position: absolute; left: 46px; top: 88px; color: var(--text-light); font-size: 11px; list-style: none; }
  .contact li { display: flex; align-items: center; gap: 5px; margin-bottom: 4px; }
  .contact svg { width: 13px; height: 13px; }

  .brand-band {
    position: absolute; left: 0; right: 0; top: 158px; bottom: 0;
    display: flex; align-items: center; justify-content: center;
  }
  .brand-name {
    font-weight: 700; font-size: 27px; letter-spacing: 1px;
    text-transform: uppercase; color: var(--brand-red);
  }

  .back-content {
    position: absolute; inset: 0;
    display: flex; flex-direction: column; align-items: center; justify-content: center;
    color: var(--text-light);
  }
  .back-content .brand-name { color: var(--text-light); font-size: 28px; }
  .credentials { margin-top: 12px; font-size: 12px; font-weight: 500; letter-spacing: 1px; word-spacing: 2px; }
  .credentials span + span { margin-left: 14px; }
</style>
</head>
<body>
<main class="canvas">
  <section class="card card--front">
    <div class="tile-field" role="img" aria-label="Blue decorative tile pattern background"></div>
    <div class="holder">
      <p class="holder__name">Tomas Vereker</p>
      <p class="holder__role">Owner/ Founder</p>
    </div>
    <ul class="contact">
      <li>
        <svg viewBox="0 0 14 14"><rect x="0.5" y="0.5" width="13" height="13" rx="2" fill="#fff"/><rect x="4.5" y="2.5" width="5" height="9" rx="1" fill="var(--tile-blue)"/><rect x="5.5" y="3.5" width="3" height="5" fill="#fff"/></svg>
        <span>04958142</span>
      </li>
      <li>
        <svg viewBox="0 0 14 14"><rect x="0.5" y="0.5" width="13" height="13" rx="2" fill="#fff"/><rect x="2.5" y="4" width="9" height="6" fill="none" stroke="var(--tile-blue)" stroke-width="1"/><path d="M2.5 4 L7 7.5 L11.5 4" fill="none" stroke="var(--tile-blue)" stroke-width="1"/></svg>
        <span>corvelltiling@brindlemail.com</span>
      </li>
    </ul>
    <div class="brand-band">
      <p class="brand-name">Corvell Tiling Solutions</p>
    </div>
  </section>

  <section class="card card--back">
    <div class="tile-field" role="img" aria-label="Blue decorative tile pattern background"></div>
    <div class="back-content">
      <p class="brand-name">Corvell Tiling Solutions</p>
      <p class="credentials"><span>QBCC 8471302</span><span>ABN 48290517736</span></p>
    </div>
  </section>
</main>
</body>
</html>
```